Halloway Crest Backers Guild business cards

Create a single-sided business card for the Halloway Crest Backers Guild based on the attached logo.
The additional data fields include Name, Title, Email, Phone, and website.
Please use the following as sample data:
Name: Dean Varrow
Title: Co-Founder / Investor
Email: deanvarrow@mailtern.net
Phone: 555-314-2706
Website: www.hcbackersguild.com

Target Market(s)

Start ups, entrepreneurs, venture capitalists

Industry/Entity Type

Investment

Contact Information for Business Card

Professional business card. Technology company.

Font styles to use
Serif
Sans Serif

Requirements
Must have
• Include the HCBG logo (attached)
• Name
• Title
• Email
• Phone
• Website
Should not have
• Cute, cartoony

```html
<!DOCTYPE html>
<html lang="en">
<head>
<meta charset="utf-8">
<title>Halloway Crest Backers Guild – Business Card</title>
<link rel="stylesheet" href="https://fonts.googleapis.com/css2?family=Open+Sans:wght@400;600&family=Tinos:wght@400;700&display=swap">
<style>
  :root {
    --page: #e9e7e3;
    --card: #ffffff;
    --green: #2fa85a;
    --green-line: #7cc993;
    --ink: #555555;
    --ink-soft: #6b6b6b;
    --rule: #8a8a8a;
  }
  * { margin: 0; padding: 0; box-sizing: border-box; }
  html, body { width: 1200px; height: 858px; overflow: hidden; }
  body {
    background: var(--page);
    position: relative;
    font-family: "Open Sans", sans-serif;
  }
  .card {
    position: absolute;
    left: 290px;
    width: 620px;
    height: 354px;
    background: var(--card);
    box-shadow: 0 2px 10px rgba(0,0,0,0.12);
  }
  .card-front { top: 56px; }
  .card-back { top: 448px; }

  /* Brand lockup: square + name, one colour, one weight */
  .brand {
    position: absolute;
    display: flex;
    align-items: center;
    gap: 14px;
  }
  .brand-mark {
    width: 18px;
    height: 18px;
    background: var(--green);
    flex: none;
  }
  .brand-divider {
    width: 1px;
    align-self: stretch;
    background: var(--green-line);
  }
  .brand-name {
    font-family: "Open Sans", sans-serif;
    font-weight: 400;
    color: var(--green);
    line-height: 1.15;
  }

  .card-front .brand { left: 44px; top: 82px; height: 62px; }
  .card-front .brand-name { font-size: 22px; }

  .holder {
    position: absolute;
    right: 46px;
    top: 44px;
    text-align: right;
    font-family: "Tinos", serif;
  }
  .holder-name {
    font-weight: 700;
    font-size: 26px;
    color: var(--green);
    line-height: 1;
  }
  .holder-title {
    font-size: 13px;
    color: var(--ink);
    margin-top: 3px;
  }

  .card-rule {
    position: absolute;
    left: 64px;
    top: 196px;
    width: 350px;
    height: 1px;
    background: var(--rule);
  }

  .contacts {
    position: absolute;
    left: 64px;
    top: 226px;
    list-style: none;
    font-family: "Tinos", serif;
    font-size: 16px;
    color: var(--ink-soft);
  }
  .contacts li {
    display: flex;
    align-items: center;
    gap: 12px;
    height: 28px;
  }
  .contact-icon {
    width: 16px;
    height: 16px;
    flex: none;
  }

  .card-back .brand {
    left: 0; right: 0; top: 0; bottom: 0;
    justify-content: center;
  }
  .card-back .brand-inner {
    display: flex;
    align-items: center;
    gap: 16px;
    height: 76px;
  }
  .card-back .brand-mark { width: 22px; height: 22px; }
  .card-back .brand-name { font-size: 30px; }
</style>
</head>
<body>

<section class="card card-front" aria-label="Business card front">
  <div class="brand">
    <span class="brand-mark"></span>
    <span class="brand-divider"></span>
    <span class="brand-name">Halloway Crest<br>Backers Guild</span>
  </div>

  <div class="holder">
    <p class="holder-name">Dean Varrow</p>
    <p class="holder-title">Co-Founder / Investor</p>
  </div>

  <div class="card-rule"></div>

  <ul class="contacts">
    <li>
      <svg class="contact-icon" viewBox="0 0 16 16" aria-hidden="true">
        <rect width="16" height="16" fill="#2fa85a"/>
        <path d="M5 3.5l2 2-1 1.2c.6 1.3 1.6 2.3 2.9 2.9l1.1-1 2 2-1.3 1.4C7.5 11.7 4.3 8.5 3.6 5z" fill="#fff"/>
      </svg>
      <span>555-314-2706</span>
    </li>
    <li>
      <svg class="contact-icon" viewBox="0 0 16 16" aria-hidden="true">
        <rect width="16" height="16" fill="#2fa85a"/>
        <rect x="3" y="4.5" width="10" height="7" fill="none" stroke="#fff" stroke-width="1.2"/>
        <path d="M3 4.5l5 4 5-4" fill="none" stroke="#fff" stroke-width="1.2"/>
      </svg>
      <span>deanvarrow@mailtern.net</span>
    </li>
    <li>
      <svg class="contact-icon" viewBox="0 0 16 16" aria-hidden="true">
        <rect width="16" height="16" fill="#2fa85a"/>
        <circle cx="8" cy="8" r="4.5" fill="none" stroke="#fff" stroke-width="1.1"/>
        <ellipse cx="8" cy="8" rx="2" ry="4.5" fill="none" stroke="#fff" stroke-width="1"/>
        <path d="M3.5 8h9" stroke="#fff" stroke-width="1"/>
      </svg>
      <span>www.hcbackersguild.com</span>
    </li>
  </ul>
</section>

<section class="card card-back" aria-label="Business card back">
  <div class="brand">
    <div class="brand-inner">
      <span class="brand-mark"></span>
      <span class="brand-divider"></span>
      <span class="brand-name">Halloway Crest<br>Backers Guild</span>
    </div>
  </div>
</section>

</body>
</html>
```